Flyer-Design für Kinderklavierunterricht gesucht
Zielgruppe
Ich unterrichte Klavier und spreche Eltern an, da ich am liebsten Kinder unterrichte.
Aufgabenstellung
Ein Din A 4 Flyer, den ich an Spielplätzen oder Kitas aushängen kann. Weil der Flyer Eltern ansprechen soll und auch in Restaurants aufgehängt wird, darf er ruhig hochwertiger als übliche Spielplatzflyer aussehen. Ich wünsche mir ein einfaches Bild in Farbe mit wenig Text, der es auf den Punkt bringt.
Ich habe 3 Fotos als Bildmaterial angehängt, Foto 2 und Foto 3 gefallen mir besser als Foto 1. Ich lasse mich auch gerne vom Gegenteil überzeugen.
Ich habe noch 2 weitere Flyer angehängt. Den 1. Flyer habe ich früher verwendet, aber er ist zu klein und doppelseitig bedruckt.
Der 2. Flyer ist, offensichtlich, schnell selbst gemacht und dient hier zum als Inspiration für den Text.
Der Text soll kurz und knapp aussagen, dass ich richtig guten Klavierunterricht anbiete, mit Patenschaft.
Der Flyer, der ein Aushang sein soll, soll keine „Abreisszettelchen“ haben.
Die Telefonnummer, Webseite und „Unterricht in der Bonner Altstadt“ soll drauf.
Der Flyer darf auch gerne an meine Webseite angelehnt sein: www.lisamerkow.com.

```html
<!DOCTYPE html>
<html lang="de">
<head>
<meta charset="utf-8">
<title>Klavierunterricht mit Patenschaft – Lisa Merkow</title>
<link rel="stylesheet" href="https://fonts.googleapis.com/css2?family=Cormorant+Garamond:wght@600&family=Open+Sans:ital,wght@0,400;0,700;1,400&display=swap">
<style>
  :root {
    --paper: #f8f9f8;
    --teal: #2b7f7b;
    --teal-light: #3f9b98;
    --grey: #e4e5e4;
    --ink: #1e1e1e;
    --white: #ffffff;
  }
  html, body { margin: 0; padding: 0; overflow: hidden; background: var(--paper); }
  .flyer {
    position: relative;
    width: 742px;
    height: 1200px;
    overflow: hidden;
    background: var(--paper);
    font-family: "Open Sans", Arial, sans-serif;
    color: var(--ink);
  }
  .shapes { position: absolute; inset: 0; }
  .brand {
    position: absolute;
    left: 40px; top: 170px;
    display: flex; align-items: center; gap: 10px;
    margin: 0;
    font-family: "Open Sans", Arial, sans-serif;
    font-weight: 700;
    font-size: 20px;
    color: var(--white);
  }
  .brand-dot {
    width: 14px; height: 14px;
    border-radius: 50%;
    background: var(--white);
  }
  .headline {
    position: absolute;
    left: 0; right: 0; top: 612px;
    margin: 0;
    text-align: center;
    font-family: "Cormorant Garamond", Georgia, serif;
    font-weight: 600;
    font-size: 29px;
    letter-spacing: 2px;
    color: var(--ink);
  }
  .benefits { list-style: none; margin: 0; padding: 0; }
  .benefit {
    position: absolute;
    font-style: italic;
    font-size: 17px;
    line-height: 22px;
    padding-left: 32px;
    white-space: nowrap;
  }
  .benefit::before {
    content: "";
    position: absolute;
    left: 2px; top: 4px;
    width: 11px; height: 11px;
    border: 2px solid var(--teal-light);
    transform: rotate(45deg);
  }
  .benefit-1 { left: 50px;  top: 676px; }
  .benefit-2 { left: 238px; top: 766px; }
  .benefit-3 { left: 318px; top: 860px; }
  .benefit-4 { left: 352px; top: 950px; }
  .contact {
    position: absolute;
    right: 32px; top: 1042px;
    text-align: right;
    color: var(--white);
    font-size: 17px;
    line-height: 26px;
    margin: 0;
  }
  .contact strong { font-weight: 700; }
</style>
</head>
<body>
<div class="flyer">
  <svg class="shapes" width="742" height="1200" viewBox="0 0 742 1200">
    <defs>
      <linearGradient id="hero-tone" x1="0" y1="0" x2="1" y2="1">
        <stop offset="0" stop-color="#e2b98c"/>
        <stop offset="0.45" stop-color="#c9a27a"/>
        <stop offset="0.75" stop-color="#3f5d88"/>
        <stop offset="1" stop-color="#b98a55"/>
      </linearGradient>
      <linearGradient id="portrait-tone" x1="0" y1="0" x2="1" y2="1">
        <stop offset="0" stop-color="#e9b78a"/>
        <stop offset="0.55" stop-color="#c98e62"/>
        <stop offset="1" stop-color="#2d3566"/>
      </linearGradient>
      <clipPath id="portrait-clip"><circle cx="50" cy="1010" r="272"/></clipPath>
    </defs>

    <path class="hero-photo" role="img" aria-label="Foto: Klavierlehrerin lehnt lachend am geöffneten Flügel, ein Kind liest Noten"
          d="M0 0 H742 V415 C610 520 350 580 0 540 Z" fill="url(#hero-tone)"/>
    <path class="swoosh-grey" d="M0 540 C350 580 610 520 742 415 V440 C612 545 350 590 0 549 Z" fill="var(--grey)"/>
    <path class="swoosh-teal" d="M0 549 C350 590 612 545 742 440 V468 C622 565 350 602 0 558 Z" fill="var(--teal)"/>

    <circle class="arc-grey" cx="95" cy="995" r="345" fill="var(--grey)"/>
    <path class="arc-white" d="M330 1200 C400 1080 380 900 250 760 C420 880 460 1060 400 1200 Z" fill="var(--paper)"/>
    <circle class="arc-teal" cx="78" cy="1010" r="282" fill="var(--teal)"/>
    <rect class="portrait-photo" role="img" aria-label="Foto: Klavierlehrerin sitzt lächelnd auf dem Boden vor einem Flügel"
          x="0" y="730" width="330" height="470" fill="url(#portrait-tone)" clip-path="url(#portrait-clip)"/>

    <path class="contact-panel" d="M345 1018 H742 V1200 H398 C392 1125 372 1068 345 1018 Z" fill="var(--teal-light)"/>
  </svg>

  <p class="brand"><span class="brand-dot"></span>Musikatelier Lisa Merkow</p>

  <h1 class="headline">KLAVIERUNTERRICHT MIT PATENSCHAFT</h1>

  <ul class="benefits">
    <li class="benefit benefit-1">Musik als Werkzeug zur Stärkung von Kindern<br>und ihrem Selbstbewusstsein</li>
    <li class="benefit benefit-2">Kompetent, einzigartig, individuell an die<br>Bedürfnisse angepasst und warmherzig</li>
    <li class="benefit benefit-3">Der Erfolg und die Zufriedenheit des<br>Schülers haben bei mir Priorität</li>
    <li class="benefit benefit-4">Unterricht für Schüler und Eltern, die<br>anders denken</li>
  </ul>

  <p class="contact">
    <strong>Interesse?</strong><br>
    Ich freue mich auf Ihren Anruf<br>
    <strong>Tel.: 0228-47192086</strong> oder<br>
    <strong>www.lisamerkow.com</strong><br>
    Unterricht in der Bonner Altstadt
  </p>
</div>
</body>
</html>
```